TR Hornets Dunmore (Social Media Pack & Stationary)

Create Stationary Designs as well as Social Media Designs (Twitter, Instagram & Facebook) as well as a Square and Banner Social media template... keep the logo I attached in the Ai file... I would like the blue in the TR Hornets logo to be navy blue instead of the dark blue.

Willing to give a good tip to get it done quicker

Please use the logo provided in the ai file.

Instagram account: @trhdunmore
FB account: TR Hornets Dunmore
Twitter: @trhdunmore

Target Market(s)

Parents and players

Font styles to use
Serif

Colors
0255a3
f78f20
f37122

Requirements
Must have
• Stationary
Twitter & FB heading
Template to post social media announcements
Template for pictures to post on social media
Template to post schedule
Envelop
Business Card
(All must include logo)

```html
<!DOCTYPE html>
<html lang="en">
<head>
<meta charset="utf-8">
<title>TR Hornets Dunmore – Schedule Templates</title>
<link href="https://fonts.googleapis.com/css2?family=Tinos:wght@400;700&display=swap" rel="stylesheet">
<style>
  :root {
    --orange: #ef4a23;
    --navy: #13305c;
    --white: #ffffff;
    --slate: #5f6b7a;
    --page: #ffffff;
  }
  * { box-sizing: border-box; margin: 0; padding: 0; }
  html, body { width: 752px; height: 1200px; overflow: hidden; background: var(--page); }
  body { position: relative; font-family: "Tinos", "Times New Roman", serif; }

  .template {
    position: absolute; left: 23px; width: 705px;
    background: var(--orange); overflow: hidden;
  }
  .template--banner { top: 26px; height: 395px; }
  .template--square { top: 450px; height: 705px; }

  .ball-art { position: absolute; left: 0; top: 0; }
  .template--banner .ball-art {
    width: 260px; height: 240px;
    background: radial-gradient(ellipse at 30% 30%, rgba(242,231,26,.95) 0%, rgba(242,200,40,.7) 30%, rgba(239,74,35,0) 70%);
  }
  .template--square .ball-art {
    width: 460px; height: 560px;
    background: radial-gradient(ellipse at 22% 28%, rgba(242,231,26,.95) 0%, rgba(240,210,30,.75) 35%, rgba(239,74,35,0) 72%);
  }

  .team-mark {
    position: absolute; color: var(--navy); font-weight: 700;
    line-height: 1; text-align: right; white-space: nowrap;
  }
  .team-mark__town, .team-mark__name { display: block; }
  .template--banner .team-mark { left: 272px; top: 9px; width: 162px; }
  .template--banner .team-mark__town { font-size: 13px; margin-bottom: 3px; }
  .template--banner .team-mark__name { font-size: 27px; }
  .template--square .team-mark { left: 430px; top: 20px; width: 232px; }
  .template--square .team-mark__town { font-size: 22px; margin-bottom: 4px; }
  .template--square .team-mark__name { font-size: 40px; }

  .socials { position: absolute; display: flex; justify-content: center; align-items: center; white-space: nowrap; }
  .socials__item { display: flex; align-items: center; }
  .socials__dot { border-radius: 50%; flex: none; }
  .template--banner .socials { left: 0; right: 0; top: 67px; gap: 14px; font-size: 8px; color: var(--white); }
  .template--banner .socials__item { gap: 4px; }
  .template--banner .socials__dot { width: 10px; height: 10px; background: var(--white); }

  .sheet {
    position: absolute; background: var(--white);
    box-shadow: 0 2px 6px rgba(0,0,0,.35);
  }
  .template--banner .sheet { left: 27px; top: 85px; width: 651px; height: 293px; }
  .template--square .sheet { left: 46px; top: 107px; width: 614px; height: 574px; }

  .sheet__title {
    position: absolute; left: 0; right: 0;
    display: flex; align-items: center; color: var(--orange); font-weight: 700;
  }
  .sheet__title::before, .sheet__title::after {
    content: ""; flex: 1; background: var(--orange);
  }
  .template--banner .sheet__title { top: 2px; font-size: 29px; gap: 6px; }
  .template--banner .sheet__title::before,
  .template--banner .sheet__title::after { height: 2px; }
  .template--square .sheet__title { top: 14px; font-size: 50px; gap: 8px; }
  .template--square .sheet__title::before,
  .template--square .sheet__title::after { height: 4px; }

  .template--square .socials { left: 0; right: 0; top: 544px; gap: 24px; font-size: 14px; color: var(--slate); }
  .template--square .socials__item { gap: 6px; }
  .template--square .socials__dot { width: 20px; height: 20px; border: 2px solid var(--slate); }
</style>
</head>
<body>
  <section class="template template--banner">
    <div class="ball-art" role="img" aria-label="Softball shattering into orange and yellow shards"></div>
    <div class="team-mark">
      <span class="team-mark__town">Dunmore</span>
      <span class="team-mark__name">TR Hornets</span>
    </div>
    <div class="socials">
      <span class="socials__item"><span class="socials__dot"></span>@trhdunmore</span>
      <span class="socials__item"><span class="socials__dot"></span>TR Hornets Dunmore</span>
      <span class="socials__item"><span class="socials__dot"></span>@trhdunmore</span>
    </div>
    <div class="sheet">
      <h2 class="sheet__title">SCHEDULE</h2>
    </div>
  </section>

  <section class="template template--square">
    <div class="ball-art" role="img" aria-label="Softball shattering into orange and yellow shards"></div>
    <div class="team-mark">
      <span class="team-mark__town">Dunmore</span>
      <span class="team-mark__name">TR Hornets</span>
    </div>
    <div class="sheet">
      <h2 class="sheet__title">SCHEDULE</h2>
      <div class="socials">
        <span class="socials__item"><span class="socials__dot"></span>@trhdunmore</span>
        <span class="socials__item"><span class="socials__dot"></span>TR Hornets Dunmore</span>
        <span class="socials__item"><span class="socials__dot"></span>@trhdunmore</span>
      </div>
    </div>
  </section>
</body>
</html>
```